Technical Refinement & Corporate Adaptation of AI Graphics

We have a follow-up project for you that involves technically refining existing, AI-generated graphics and recreating them professionally in Microsoft PowerPoint. - as you did already. The content and core structure should remain unchanged, but the visual style needs to be aligned with the corporate design of the Kraftwerkhaus Morlen (colors, typography, and visual language). The primary focus is to ensure all elements are fully editable, perfectly aligned, and deliver a clean, scientific-technical look.

```html
<!DOCTYPE html>
<html lang="en">
<head>
<meta charset="utf-8">
<title>Kraftwerkhaus Morlen – Analytical Modules</title>
<link href="https://fonts.googleapis.com/css2?family=Arimo:ital,wght@0,400;0,700;1,400&display=swap" rel="stylesheet">
<style>
:root{
  --green:#2e7d32;--teal:#00777f;--orange:#f07c00;--navy:#0b3a6e;--purple:#5b2a86;
  --gray:#6b7280;--blue:#3d8ab5;--ink:#222;--muted:#6f7780;--line:#d3d9df;--panel:#f5f7f8;--canvas:#f0f2f4;
}
*{box-sizing:border-box;margin:0;padding:0}
html,body{width:1200px;height:1200px;overflow:hidden;background:var(--canvas);font-family:Arimo,Arial,sans-serif;color:var(--ink)}
.slide{position:absolute;width:507px;height:286px;background:#fff;border:1px solid #cdd3d9;--accent:var(--green)}
.c1{left:86px}.c2{left:607px}.r1{top:8px}.r2{top:307px}.r3{top:607px}.r4{top:906px}
.badge{position:absolute;left:17px;top:12px;width:23px;height:23px;border-radius:50%;background:var(--accent);color:#fff;font-weight:700;font-size:11px;display:flex;align-items:center;justify-content:center}
.title{position:absolute;left:52px;top:13px;font-size:12.5px;font-weight:700;color:var(--accent);white-space:nowrap}
.subtitle{position:absolute;left:52px;top:30px;font-size:6.8px;font-style:italic;color:#333}
.rule{position:absolute;left:17px;right:17px;top:42px;height:1px;background:var(--accent)}
.footer{position:absolute;left:17px;right:17px;top:273px;border-top:1px solid var(--line);font-size:4px;padding-top:3px;color:#555}
.footer b{color:var(--navy);position:absolute;left:4px}
.footer span{position:absolute;left:200px}
.abs{position:absolute}
.finding{position:absolute;left:17px;width:473px;top:232px;height:28px;border:1px solid var(--line);border-radius:3px;background:#f8fafb}
.finding .dot{position:absolute;left:6px;top:4px;width:20px;height:20px;border-radius:50%;background:var(--green);color:#fff;font-size:10px;display:flex;align-items:center;justify-content:center}
.finding h4{position:absolute;left:39px;top:6px;font-size:5px;color:var(--green)}
.finding p{position:absolute;left:39px;top:15px;font-size:4.6px;color:#333}
/* dimension cards */
.dim{position:absolute;left:19px;width:123px;height:28px;border:1px solid var(--line);border-radius:3px;background:var(--panel);display:flex;align-items:center;gap:9px;padding-left:6px;font-size:7px;line-height:1.15}
.dim i{width:20px;height:20px;border-radius:50%;color:#fff;font-style:normal;display:flex;align-items:center;justify-content:center;font-size:9px;flex:none}
.legend{position:absolute;left:397px;font-size:6px;display:flex;align-items:center;gap:8px}
.legend i{width:12px;height:2px}
.keybox{position:absolute;left:392px;top:155px;width:91px;height:49px;border:1px solid var(--line);border-radius:3px;text-align:center;font-size:5.8px;padding-top:8px;line-height:1.25}
.keybox b{color:var(--green);display:block;margin-bottom:5px}
/* result cards */
.card{position:absolute;width:152px;height:59px;border:1px solid var(--line);border-radius:3px;background:var(--panel)}
.card .n{position:absolute;left:7px;top:7px;width:12px;height:12px;border-radius:50%;background:var(--green);color:#fff;font-size:5.5px;font-weight:700;display:flex;align-items:center;justify-content:center}
.card h5{position:absolute;left:30px;top:9px;font-size:5px;color:var(--navy)}
.card p{position:absolute;left:30px;top:20px;font-size:4.2px;color:var(--muted)}
.card .sq{position:absolute;top:33px;width:17px;height:14px}
.card .sq.b{top:38px;height:9px}
.card .flow{position:absolute;left:40px;top:35px;font-size:8px;color:var(--teal);letter-spacing:5px}
/* process slides */
.steps{position:absolute;left:17px;top:54px;width:473px;display:grid;grid-template-columns:repeat(6,1fr)}
.step{text-align:center;position:relative;height:100px}
.step .num{width:13px;height:13px;border-radius:50%;background:var(--accent);color:#fff;font-size:5px;font-weight:700;display:flex;align-items:center;justify-content:center;margin:0 auto}
.step h6{font-size:6.6px;color:var(--accent);line-height:1.15;height:24px;margin-top:4px}
.step .ico{position:absolute;left:50%;top:38px;margin-left:-12px;width:24px;height:24px;border-radius:50%;background:var(--accent);color:#fff;font-size:10px;display:flex;align-items:center;justify-content:center}
.step p{position:absolute;top:72px;left:4px;right:4px;font-size:4.8px;color:#444;line-height:1.2}
.arrow{position:absolute;top:97px;font-size:9px;color:#333}
.methods{position:absolute;left:17px;top:155px;width:473px;height:41px;border:1px solid var(--line);border-radius:3px;background:var(--panel)}
.methods h4{text-align:center;font-size:7px;color:var(--accent);margin-top:5px}
.mrow{display:grid;grid-template-columns:repeat(6,1fr);margin-top:5px;padding:0 6px}
.mrow div,.brow div{display:flex;gap:8px;align-items:flex-start;font-size:4.6px;color:#444;line-height:1.2}
.mrow em,.brow em{font-style:normal;font-size:8px;color:var(--accent);line-height:1;width:9px;text-align:center;flex:none}
.band{position:absolute;left:17px;top:204px;width:473px;height:17px;background:var(--accent);color:#fff;font-size:8px;font-weight:700;text-align:center;line-height:17px;border-radius:2px}
.brow{position:absolute;left:17px;top:229px;width:473px;display:grid;grid-template-columns:repeat(5,1fr);padding:0 8px}
.s5{--accent:var(--navy)} .s6{--accent:var(--teal)} .s7{--accent:var(--green)} .s8{--accent:var(--purple)}
.s2{--accent:var(--navy)}
/* charts */
.ctitle{position:absolute;font-size:6.8px;font-weight:700;color:#333}
.csub{position:absolute;font-size:5px;color:var(--muted)}
.small{position:absolute;font-size:4.2px;color:#555;text-align:center}
.heat{position:absolute;left:36px;top:83px;display:grid;grid-template-columns:repeat(5,14px);gap:2px}
.heat span{height:14px}
.h0{background:#dcefe9}.h1{background:#b9e0d3}.h2{background:#7cc8ae}.h3{background:#35a583}.h4{background:#0e7d6c}
.lg{position:absolute;left:34px;font-size:4.6px;display:flex;gap:8px;align-items:center}
.lg i{width:7px;height:7px}
.hbar{position:absolute;left:186px;height:13px}
.hlab{position:absolute;left:278px;font-size:4.8px;color:#333}
.vbar{position:absolute;bottom:97px}
.pv{position:absolute;left:270px;top:73px;display:grid;grid-template-columns:repeat(9,12px);gap:2px}
.pv span{height:11px}
.suit{position:absolute;left:400px;top:73px;display:grid;grid-template-columns:repeat(6,10px);gap:2px}
.suit span{height:11px}
.Y{background:#f9c74f}.L{background:#fde7a8}.O{background:#f07c00}.T{background:var(--teal)}
.g1{background:#d9ede1}.g2{background:#a3d4b6}.g3{background:#5fb496}.g4{background:#00777f}
</style>
</head>
<body>

<!-- 1 Integrated assessment -->
<section class="slide c1 r1">
  <div class="badge">1</div>
  <h1 class="title">INTEGRATED PROCESS ASSESSMENT</h1>
  <p class="subtitle">for Technology and Product Innovation</p>
  <div class="rule"></div>
  <div class="dim" style="top:52px"><i style="background:var(--green)">◒</i>Environmental<br>(LCA)</div>
  <div class="dim" style="top:88px"><i style="background:var(--teal)">€</i>Economic<br>(TEA)</div>
  <div class="dim" style="top:124px"><i style="background:var(--orange)">●●</i>Social<br>(S-LCA)</div>
  <div class="dim" style="top:160px"><i style="background:var(--gray)">⚙</i>Technical<br>(Performance)</div>
  <div class="ctitle" style="left:214px;top:53px;font-size:8.5px">Overall Sustainability Performance</div>
  <div class="small" style="left:270px;top:65px;font-size:4.6px">(normalized)</div>
  <svg class="abs" style="left:200px;top:60px" width="190" height="150" viewBox="200 60 190 150">
    <g fill="none" stroke="#d6dbe0" stroke-width="0.8">
      <circle cx="289" cy="132" r="63"/><circle cx="289" cy="132" r="49"/><circle cx="289" cy="132" r="24"/>
    </g>
    <g fill="var(--green)"><circle cx="289" cy="82" r="1.8"/><circle cx="333" cy="117" r="1.8"/><circle cx="320" cy="174" r="1.8"/><circle cx="246" cy="170" r="1.8"/><circle cx="234" cy="116" r="1.8"/></g>
    <g fill="var(--teal)"><circle cx="289" cy="78" r="1.8"/><circle cx="337" cy="113" r="1.8"/><circle cx="329" cy="180" r="1.8"/><circle cx="257" cy="176" r="1.8"/><circle cx="241" cy="111" r="1.8"/></g>
    <g fill="var(--orange)"><circle cx="289" cy="96" r="1.8"/><circle cx="324" cy="123" r="1.8"/><circle cx="312" cy="166" r="1.8"/><circle cx="261" cy="163" r="1.8"/><circle cx="247" cy="124" r="1.8"/></g>
  </svg>
  <div class="small" style="left:189px;top:106px;font-size:5px">Social Acceptance</div>
  <div class="small" style="left:359px;top:106px;font-size:5px">Costs</div>
  <div class="small" style="left:225px;top:189px;font-size:5px">Technology<br>Performance</div>
  <div class="small" style="left:318px;top:189px;font-size:5px">Resource Use</div>
  <div class="legend" style="top:91px"><i style="background:var(--green)"></i>Option A</div>
  <div class="legend" style="top:106px"><i style="background:var(--teal)"></i>Option B</div>
  <div class="legend" style="top:122px"><i style="background:var(--orange)"></i>Option C</div>
  <div class="keybox"><b>KEY FINDING</b>Option B shows the<br>best overall balance<br>across all dimensions.</div>
  <div class="finding"><div class="dot">✓</div><h4>INTEGRATED ASSESSMENT</h4><p>Integrated assessment enables robust decision-making and identifies trade-offs.</p></div>
  <div class="footer"><b>Kraftwerkhaus Morlen</b><span>Research, analysis and solutions for a secure, climate-neutral and resource-efficient future.</span></div>
</section>

<!-- Results illustrations -->
<section class="slide c2 r1 s2">
  <div class="badge">1–</div>
  <h1 class="title">RESULTS ILLUSTRATIONS</h1>
  <p class="subtitle">Consistent evidence views across nine analytical modules</p>
  <div class="rule"></div>
  <div class="card" style="left:17px;top:50px"><div class="n">1</div><h5>INTEGRATED ASSESSMENT</h5><p>Radar comparison</p>
    <svg class="abs" style="left:30px;top:32px" width="70" height="14"><line x1="0" y1="3" x2="70" y2="3" stroke="#c5ccd3" stroke-width=".6"/><line x1="0" y1="7" x2="70" y2="7" stroke="#c5ccd3" stroke-width=".6"/><line x1="0" y1="11" x2="70" y2="11" stroke="#c5ccd3" stroke-width=".6"/><rect x="40" y="3" width="5" height="5" transform="rotate(45 42.5 5.5)" fill="none" stroke="var(--teal)" stroke-width=".7"/></svg></div>
  <div class="card" style="left:176px;top:50px"><div class="n">2</div><h5>SOCIO-ECONOMIC ANALYSIS</h5><p>Acceptance &amp; impact</p><i class="sq" style="left:30px;background:var(--green)"></i><i class="sq b" style="left:58px;background:var(--teal)"></i><i class="sq" style="left:87px;background:var(--orange)"></i></div>
  <div class="card" style="left:335px;top:50px"><div class="n">3</div><h5>TECHNO-ECONOMIC ANALYSIS</h5><p>Cost &amp; sensitivity</p><i class="sq" style="left:30px;background:var(--green)"></i><i class="sq b" style="left:58px;background:var(--teal)"></i><i class="sq" style="left:87px;background:var(--orange)"></i></div>
  <div class="card" style="left:17px;top:116px"><div class="n">4</div><h5>CONCEPT PRE-ENGINEERING</h5><p>Process &amp; balances</p><div class="flow">▦→◫→◎</div></div>
  <div class="card" style="left:176px;top:116px"><div class="n">5</div><h5>MCDA</h5><p>Weighted ranking</p><i class="sq" style="left:30px;background:var(--green)"></i><i class="sq b" style="left:58px;background:var(--teal)"></i><i class="sq" style="left:87px;background:var(--orange)"></i></div>
  <div class="card" style="left:335px;top:116px"><div class="n">6</div><h5>HYDROGEN, CCUS &amp; PTX</h5><p>Efficiency &amp; emissions</p><i class="sq" style="left:30px;background:var(--green)"></i><i class="sq b" style="left:58px;background:var(--teal)"></i><i class="sq" style="left:87px;background:var(--orange)"></i></div>
  <div class="card" style="left:17px;top:183px"><div class="n">7</div><h5>ENERGY INFRASTRUCTURE</h5><p>Grid, mix &amp; storage</p><div class="flow">▦→◫→◎</div></div>
  <div class="card" style="left:176px;top:183px"><div class="n">8</div><h5>CIRCULAR ECONOMY</h5><p>Circularity &amp; impact</p><i class="sq" style="left:30px;background:var(--green)"></i><i class="sq b" style="left:58px;background:var(--teal)"></i><i class="sq" style="left:87px;background:var(--orange)"></i></div>
  <div class="card" style="left:335px;top:183px"><div class="n">9</div><h5>GIS SITE ANALYSIS</h5><p>Potential &amp; suitability</p><div class="flow" style="left:52px;color:var(--green);letter-spacing:3px;font-weight:700">▧◉123</div></div>
  <div class="footer"><b>Kraftwerkhaus Morlen</b><span>Research, analysis and solutions for a secure, climate-neutral and resource-efficient future.</span></div>
</section>

<!-- 7 Energy infrastructure -->
<section class="slide c1 r2">
  <div class="badge">7</div>
  <h1 class="title">ENERGY INFRASTRUCTURE</h1>
  <p class="subtitle">2035 system requirements and operating patterns</p>
  <div class="rule"></div>
  <div class="ctitle" style="left:23px;top:56px">Grid Expansion Need (2035)</div>
  <div class="csub" style="left:23px;top:66px">Load increase vs. today (%)</div>
  <div class="heat">
    <span class="h0"></span><span class="h1"></span><span class="h0"></span><span class="h1"></span><span class="h2"></span>
    <span class="h1"></span><span class="h1"></span><span class="h2"></span><span class="h3"></span><span class="h2"></span>
    <span class="h0"></span><span class="h2"></span><span class="h3"></span><span class="h3"></span><span class="h1"></span>
    <span class="h1"></span><span class="h3"></span><span class="h4"></span><span class="h2"></span><span class="h0"></span>
    <span class="h0"></span><span class="h1"></span><span class="h2"></span><span class="h1"></span><span class="h0"></span>
  </div>
  <div class="lg" style="top:179px"><i class="h0"></i>&lt; 10</div>
  <div class="lg" style="top:189px"><i class="h1"></i>10–25</div>
  <div class="lg" style="top:199px"><i class="h2"></i>25–50</div>
  <div class="lg" style="top:209px"><i class="h3"></i>50–75</div>
  <div class="lg" style="top:219px"><i class="h4"></i>&gt; 75</div>
  <div class="ctitle" style="left:178px;top:56px">Generation Mix (2035)</div>
  <i class="hbar" style="top:84px;width:68px;background:var(--green)"></i><span class="hlab" style="top:88px">Wind 34%</span>
  <i class="hbar" style="top:103px;width:68px;background:var(--orange)"></i><span class="hlab" style="top:107px">Solar 28%</span>
  <i class="hbar" style="top:122px;width:44px;background:var(--teal)"></i><span class="hlab" style="top:126px">Hydro 18%</span>
  <i class="hbar" style="top:141px;width:25px;background:var(--gray)"></i><span class="hlab" style="top:145px">Gas 10%</span>
  <i class="hbar" style="top:160px;width:25px;background:#8cc56f"></i><span class="hlab" style="top:164px">Biomass 10%</span>
  <div class="ctitle" style="left:346px;top:56px">Storage Utilization</div>
  <div class="csub" style="left:346px;top:66px">Full-load hours</div>
  <i class="vbar" style="left:354px;width:19px;height:55px;background:var(--green)"></i><span class="small" style="left:354px;width:19px;top:126px">2.20</span><span class="small" style="left:348px;width:31px;top:195px">Battery</span>
  <i class="vbar" style="left:385px;width:19px;height:108px;background:var(--teal)"></i><span class="small" style="left:385px;width:19px;top:73px">4.40</span><span class="small" style="left:379px;width:31px;top:195px">P2G</span>
  <i class="vbar" style="left:416px;width:19px;height:76px;background:var(--orange)"></i><span class="small" style="left:416px;width:19px;top:105px">3.10</span><span class="small" style="left:410px;width:31px;top:195px">Thermal</span>
  <i class="vbar" style="left:447px;width:19px;height:124px;background:var(--blue)"></i><span class="small" style="left:447px;width:19px;top:57px">5.00</span><span class="small" style="left:441px;width:31px;top:195px">Hydro</span>
  <div class="finding"><div class="dot">↯</div><h4>KEY FINDING</h4><p>High shares of wind and solar require storage and grid expansion, with P2G and hydro providing seasonal flexibility.</p></div>
  <div class="footer"><b>Kraftwerkhaus Morlen</b><span>Research, analysis and solutions for a secure, climate-neutral and resource-efficient future.</span></div>
</section>

<!-- 8 Circular economy & GIS -->
<section class="slide c2 r2">
  <div class="badge">8–</div>
  <h1 class="title">CIRCULAR ECONOMY &amp; GIS-BASED SITE ANALYSIS</h1>
  <p class="subtitle">Material performance and spatial potential in one evidence framework</p>
  <div class="rule"></div>
  <div class="ctitle" style="left:23px;top:56px;color:var(--navy)">INDUSTRIAL PROCESSES &amp; CIRCULAR ECONOMY</div>
  <div class="ctitle" style="left:263px;top:56px;color:var(--navy)">GIS-BASED SITE &amp; POTENTIAL ANALYSIS</div>
  <div class="csub" style="left:23px;top:71px;font-weight:700;color:#333">Material Circularity Indicator (MCI)</div>
  <div class="csub" style="left:143px;top:71px;font-weight:700;color:#333">Environmental impact</div>
  <i class="vbar" style="bottom:124px;left:31px;width:17px;height:24px;background:var(--green)"></i><span class="small" style="left:27px;width:25px;top:133px">0.28</span><span class="small" style="left:25px;width:29px;top:165px">Product A</span>
  <i class="vbar" style="bottom:124px;left:59px;width:17px;height:38px;background:var(--teal)"></i><span class="small" style="left:55px;width:25px;top:119px">0.46</span><span class="small" style="left:53px;width:29px;top:165px">Product B</span>
  <i class="vbar" style="bottom:124px;left:87px;width:17px;height:60px;background:var(--orange)"></i><span class="small" style="left:83px;width:25px;top:97px">0.72</span><span class="small" style="left:81px;width:29px;top:165px">Product C</span>
  <i class="vbar" style="bottom:124px;left:115px;width:17px;height:74px;background:var(--gray)"></i><span class="small" style="left:111px;width:25px;top:83px">0.90</span><span class="small" style="left:109px;width:29px;top:165px">Target</span>
  <i class="vbar" style="bottom:124px;left:154px;width:28px;height:74px;background:var(--gray)"></i><span class="small" style="left:155px;width:25px;top:83px">1.00</span><span class="small" style="left:153px;width:29px;top:165px">Current</span>
  <i class="vbar" style="bottom:124px;left:197px;width:28px;height:38px;background:var(--teal)"></i><span class="small" style="left:198px;width:25px;top:119px">0.48</span><span class="small" style="left:196px;width:29px;top:165px">Circular</span>
  <div class="pv">
    <span class="Y"></span><span class="O"></span><span class="Y"></span><span class="T"></span><span class="L"></span><span class="T"></span><span class="O"></span><span class="O"></span><span class="L"></span>
    <span class="O"></span><span class="Y"></span><span class="O"></span><span class="T"></span><span class="L"></span><span class="Y"></span><span class="O"></span><span class="T"></span><span class="L"></span>
    <span class="O"></span><span class="O"></span><span class="T"></span><span class="L"></span><span class="Y"></span><span class="Y"></span><span class="O"></span><span class="T"></span><span class="L"></span>
    <span class="O"></span><span class="T"></span><span class="Y"></span><span class="L"></span><span class="Y"></span><span class="T"></span><span class="L"></span><span class="O"></span><span class="Y"></span>
    <span class="T"></span><span class="L"></span><span class="Y"></span><span class="Y"></span><span class="T"></span><span class="L"></span><span class="Y"></span><span class="Y"></span><span class="T"></span>
    <span class="Y"></span><span class="O"></span><span class="T"></span><span class="Y"></span><span class="L"></span><span class="Y"></span><span class="O"></span><span class="Y"></span><span class="O"></span>
  </div>
  <div class="suit">
    <span class="g1"></span><span class="g2"></span><span class="g3"></span><span class="g3"></span><span class="g2"></span><span class="g4"></span>
    <span class="g2"></span><span class="g3"></span><span class="g4"></span><span class="g1"></span><span class="g2"></span><span class="g2"></span>
    <span class="g4"></span><span class="g1"></span><span class="g2"></span><span class="g3"></span><span class="g2"></span><span class="g3"></span>
    <span class="g2"></span><span class="g3"></span><span class="g4"></span><span class="g3"></span><span class="g1"></span><span class="g2"></span>
    <span class="g3"></span><span class="g4"></span><span class="g2"></span><span class="g1"></span><span class="g2"></span><span class="g3"></span>
    <span class="g1"></span><span class="g2"></span><span class="g3"></span><span class="g2"></span><span class="g2"></span><span class="g4"></span>
  </div>
  <div class="csub" style="left:273px;top:161px;font-weight:700;color:#333">Solar PV potential</div>
  <div class="csub" style="left:402px;top:161px;font-weight:700;color:#333">Suitability score</div>
  <div class="finding"><div class="dot">◎</div><h4>KEY FINDING</h4><p>Circular strategies improve material circularity and reduce impacts; GIS screening identifies high-potential sites with limited constraints.</p></div>
  <div class="footer"><b>Kraftwerkhaus Morlen</b><span>Research, analysis and solutions for a secure, climate-neutral and resource-efficient future.</span></div>
</section>

<!-- 5 Business models -->
<section class="slide c1 r3 s5">
  <div class="badge">5</div>
  <h1 class="title">BUSINESS MODELS, GOVERNANCE &amp; IMPLEMENTATION</h1>
  <p class="subtitle">From concepts to successful and scalable implementation</p>
  <div class="rule"></div>
  <div class="steps">
    <div class="step"><div class="num">1</div><h6>Stakeholders &amp;<br>Ecosystem</h6><div class="ico">●●</div><p>Actors, roles, partnerships, public acceptance</p></div>
    <div class="step"><div class="num">2</div><h6>Value Proposition<br>&amp; Value Chains</h6><div class="ico">➚</div><p>Customer needs, services, resources, value flows</p></div>
    <div class="step"><div class="num">3</div><h6>Business Model<br>Design</h6><div class="ico">▦</div><p>Revenues, costs, risks, key resources</p></div>
    <div class="step"><div class="num">4</div><h6>Market &amp;<br>Regulatory Framework</h6><div class="ico">⚖</div><p>Policies, incentives, market rules, permits</p></div>
    <div class="step"><div class="num">5</div><h6>Implementation</h6><div class="ico">⚑</div><p>Pilots, scaling, financing, roll-out strategies</p></div>
    <div class="step"><div class="num">6</div><h6>Monitoring &amp;<br>Adaptation</h6><div class="ico">⌁</div><p>KPIs, learning, adaptation and improvement</p></div>
  </div>
  <span class="arrow" style="left:92px">→</span><span class="arrow" style="left:171px">→</span><span class="arrow" style="left:250px">→</span><span class="arrow" style="left:329px">→</span><span class="arrow" style="left:408px">→</span>
  <div class="methods"><h4>METHODS &amp; TOOLS</h4><div class="mrow">
    <div><em>◉</em>Stakeholder analysis</div><div><em>▦</em>Business model canvas</div><div><em>▥</em>Financial &amp; economic analysis</div><div><em>△</em>Risk &amp; barrier assessment</div><div><em>▤</em>Governance &amp; policy analysis</div><div><em>⚖</em>MCDA</div></div></div>
  <div class="band">BENEFITS &amp; RESULTS</div>
  <div class="brow"><div><em>€</em>Bankable and viable solutions</div><div><em>●</em>Clear value for all stakeholders</div><div><em>◇</em>Reduced risks and barriers</div><div><em>◴</em>Faster and smoother implementation</div><div><em>▥</em>Long-term success and scalability</div></div>
  <div class="footer"><b>Kraftwerkhaus Morlen</b><span>Research, analysis and solutions for a secure, climate-neutral and resource-efficient future.</span></div>
</section>

<!-- 2 GIS -->
<section class="slide c2 r3 s6">
  <div class="badge">2</div>
  <h1 class="title">GIS-BASED SITE &amp; POTENTIAL ASSESSMENT</h1>
  <p class="subtitle">Data-driven insights for optimal locations and infrastructure</p>
  <div class="rule"></div>
  <div class="steps">
    <div class="step"><div class="num">1</div><h6>Data Collection<br>&amp; Preparation</h6><div class="ico">▱</div><p>Spatial data, networks, demand, environment</p></div>
    <div class="step"><div class="num">2</div><h6>Constraint &amp;<br>Restriction Analysis</h6><div class="ico">!</div><p>Technical, legal, environmental, social limits</p></div>
    <div class="step"><div class="num">3</div><h6>Potential<br>Assessment</h6><div class="ico">▥</div><p>Generation, storage, demand, resources</p></div>
    <div class="step"><div class="num">4</div><h6>Site Evaluation<br>(MCDA)</h6><div class="ico">⚖</div><p>Multi-criteria comparison and scoring</p></div>
    <div class="step"><div class="num">5</div><h6>Suitability<br>Mapping</h6><div class="ico">▧</div><p>High-resolution maps and heatmaps</p></div>
    <div class="step"><div class="num">6</div><h6>Prioritization &amp;<br>Roadmap</h6><div class="ico"></div><p>Phasing, ranking, and investment plan</p></div>
  </div>
  <span class="arrow" style="left:92px">→</span><span class="arrow" style="left:171px">→</span><span class="arrow" style="left:250px">→</span><span class="arrow" style="left:329px">→</span><span class="arrow" style="left:408px">→</span>
  <div class="methods"><h4>METHODS &amp; TOOLS</h4><div class="mrow" style="grid-template-columns:repeat(5,1fr)">
    <div><em>◎</em>GIS &amp; spatial analysis</div><div><em>▤</em>Geospatial databases</div><div><em>⌘</em>Network &amp; flow analysis</div><div><em>△</em>Multi-criteria analysis (MCDA)</div><div><em>▧</em>Scenario-based mapping</div></div></div>
  <div class="band">BENEFITS &amp; RESULTS</div>
  <div class="brow"><div><em></em>Best locations for infrastructure and technologies</div><div><em>◒</em>Efficient use of resources and land</div><div><em>◇</em>Reduced risks and conflicts</div><div><em>▥</em>Transparent and reproducible evaluation</div><div><em>✓</em>Support for planning and permit processes</div></div>
  <div class="footer"><b>Kraftwerkhaus Morlen</b><span>Research, analysis and solutions for a secure, climate-neutral and resource-efficient future.</span></div>
</section>

<!-- 1 Scenario -->
<section class="slide c1 r4 s7">
  <div class="badge">1</div>
  <h1 class="title">SCENARIO &amp; TRANSFORMATION PATHWAY ANALYSIS</h1>
  <p class="subtitle">Shaping robust options for a climate-neutral future</p>
  <div class="rule"></div>
  <div class="steps">
    <div class="step"><div class="num">1</div><h6>Scenario<br>Framework</h6><div class="ico">◎</div><p>Reference and target scenarios</p></div>
    <div class="step"><div class="num">2</div><h6>Assumptions &amp;<br>Data</h6><div class="ico">▤</div><p>Technologies, policies, markets, society, climate</p></div>
    <div class="step"><div class="num">3</div><h6>Demand, Prices &amp;<br>Resources</h6><div class="ico">⌁</div><p>Energy demand, prices, resources and constraints</p></div>
    <div class="step"><div class="num">4</div><h6>Milestones &amp;<br>Timing</h6><div class="ico">⚑</div><p>Technology change, timing, key milestones</p></div>
    <div class="step"><div class="num">5</div><h6>Uncertainty &amp;<br>Sensitivity</h6><div class="ico">◉</div><p>Sensitivity analysis and robustness checks</p></div>
    <div class="step"><div class="num">6</div><h6>Insights &amp;<br>Decisions</h6><div class="ico">↔</div><p>No-regret measures and strategy options</p></div>
  </div>
  <span class="arrow" style="left:92px">→</span><span class="arrow" style="left:171px">→</span><span class="arrow" style="left:250px">→</span><span class="arrow" style="left:329px">→</span><span class="arrow" style="left:408px">→</span>
  <div class="methods"><h4>METHODS &amp; TOOLS</h4><div class="mrow" style="grid-template-columns:repeat(5,1fr)">
    <div><em>▦</em>Energy system models</div><div><em>⚙</em>Optimization &amp; simulation</div><div><em>↕</em>Bottom-up &amp; top-down approaches</div><div><em>⬡</em>Monte Carlo &amp; robustness</div><div><em>▥</em>Visualization &amp; dashboards</div></div></div>
  <div class="band">BENEFITS &amp; RESULTS</div>
  <div class="brow"><div><em>◇</em>Robust options under uncertainty</div><div><em>⚖</em>Transparent assumptions &amp; trade-offs</div><div><em>◉</em>Identification of key levers and risks</div><div><em>●</em>Support for policy, investment and strategic planning</div><div><em>◎</em>Alignment with climate targets and security of supply</div></div>
  <div class="footer"><b>Kraftwerkhaus Morlen</b><span>Research, analysis and solutions for a secure, climate-neutral and resource-efficient future.</span></div>
</section>

<!-- 4 District heating -->
<section class="slide c2 r4 s8">
  <div class="badge">4</div>
  <h1 class="title">DISTRICT HEATING, WASTE HEAT &amp; THERMAL STORAGE</h1>
  <p class="subtitle">Efficient and sustainable heat solutions for industry and communities</p>
  <div class="rule"></div>
  <div class="steps">
    <div class="step"><div class="num">1</div><h6>Heat Sources</h6><div class="ico">♨</div><p>Industrial waste heat, geothermal, solar thermal, CHP, heat pumps, P2H</p></div>
    <div class="step"><div class="num">2</div><h6>Conversion &amp;<br>Upgrading</h6><div class="ico">▥</div><p>Heat pumps, boiler, electric heaters, steam systems</p></div>
    <div class="step"><div class="num">3</div><h6>Thermal Storage</h6><div class="ico">◒</div><p>Short-term hot water, sensible, latent, thermochemical</p></div>
    <div class="step"><div class="num">4</div><h6>Heat Networks</h6><div class="ico">⌁</div><p>District heating and low-temperature networks</p></div>
    <div class="step"><div class="num">5</div><h6>End Uses</h6><div class="ico">▦</div><p>Industry, buildings, services, public facilities</p></div>
    <div class="step"><div class="num">6</div><h6>Optimization &amp;<br>Operation</h6><div class="ico">⚙</div><p>Load matching, control strategies, flexibility</p></div>
  </div>
  <span class="arrow" style="left:92px">→</span><span class="arrow" style="left:171px">→</span><span class="arrow" style="left:250px">→</span><span class="arrow" style="left:329px">→</span><span class="arrow" style="left:408px">→</span>
  <div class="methods"><h4>METHODS &amp; TOOLS</h4><div class="mrow">
    <div><em>◒</em>Energy &amp; exergy analysis</div><div><em>⌘</em>Network modeling</div><div><em>€</em>Techno-economic assessment (TEA)</div><div><em>✣</em>eLCA</div><div><em>⚙</em>Optimization &amp; simulation</div><div><em>⌁</em>Sensitivity &amp; scenario analysis</div></div></div>
  <div class="band">BENEFITS &amp; RESULTS</div>
  <div class="brow"><div><em>▥</em>Higher energy efficiency</div><div><em>◒</em>Lower emissions and costs</div><div><em>♨</em>Better use of waste heat resources</div><div><em>◇</em>Resilient and flexible heat supply</div><div><em>●</em>Support for industrial and urban transformation</div></div>
  <div class="footer"><b>Kraftwerkhaus Morlen</b><span>Research, analysis and solutions for a secure, climate-neutral and resource-efficient future.</span></div>
</section>

</body>
</html>
```